Icons for a Major Sports App

This is to be a clean and simple monochromatic design. The three grays in the arrows of the logo are to be used. The blue in the logo should NOT be used.

The following Toolbars will be an overlay on a video and should be opaque as possible

Toolbar A: Pencil, Location, Weather, Microphone, Compare (a function to compare to videos side by side), Lumiverse Post and Quillo Post

Toolbar B: Line, Squiggle, Circle, Square, Wedge (to measure and angle), circle with two parallel lines touching the outside (sway in golf terms),Toggle between Red, Blue, Green, White, Erase All, Erase One at time

Toolbar Audio (Play, Pause, Stop, Save, Delete, cancel)

Toolbar Video (Play, Pause, Step forward, Step back, Normal Speed, ½ speed)

The following will be used for Navigation at the bottom of the application in many screens. The Screen the user is on should be highlighted from the other Icon’s

Tab: Main, Clubhouse, Setting

Buttons: Light gray, Silver and Dark Gray (see colors in Uploaded Logo)

Icons:
• Video
• Camera Shutter
• User
• Users
• Golfer
• Help
• Favorite
• Next
• Previous
• Log-In
• Sign-Up
• Password
Four versions in each size (White, Light Gray , Silver and Dark Gray, see colors in Uploaded Logo)

Camera

Requirements
Must have
• Submissions should meet Korvens zQR Human Interface Standards http://builders.korvenhub.net/library/zqr/#documentation/userexperience/conceptual/mobileguide/IconsImages/IconsImages.html
Need Graphics for:
• Vantel 5 and Brisa glide (5th generation)
• high-resolution Vantel and Brisa glide
• Vantel and Brisa glide
• high-resolution Morda
• Morda

```html
<!DOCTYPE html>
<html lang="en">
<head>
<meta charset="utf-8">
<title>Video</title>
<link rel="stylesheet" href="https://fonts.googleapis.com/css2?family=Source+Sans+3:wght@400;600;700&family=Inter:wght@400;500&display=swap">
<style>
  :root {
    --nav-top: #6a98d6;
    --nav-bottom: #3b6db3;
    --nav-line: #2c4f82;
    --btn-top: #4f82c6;
    --btn-bottom: #2f5f9f;
    --white: #ffffff;
    --sky-top: #5d8fd8;
    --sky-mid: #dfe8f2;
    --field: #8fae6a;
    --grass: #4f7a32;
    --panel: rgba(112, 112, 112, 0.78);
    --panel-edge: rgba(255, 255, 255, 0.18);
    --icon: #d2d2d2;
    --icon-cut: #666666;
    --tab-active: #474747;
    --tab-top: #ffffff;
    --tab-bottom: #e6e6e6;
    --tab-text: #3a3a3a;
    --tab-divider: #c4c4c4;
  }
  * { box-sizing: border-box; margin: 0; padding: 0; }
  html, body { width: 835px; height: 1200px; overflow: hidden; background: #ffffff; }
  .screen { position: relative; width: 835px; height: 1200px; overflow: hidden; }

  .nav-bar {
    position: absolute; left: 0; top: 0; width: 835px; height: 116px;
    background: linear-gradient(var(--nav-top), var(--nav-bottom));
    border-bottom: 2px solid var(--nav-line);
    z-index: 2;
  }
  .nav-title {
    position: absolute; left: 0; right: 0; top: 32px; text-align: center;
    font-family: "Source Sans 3", sans-serif; font-weight: 700; font-size: 41px;
    color: var(--white); text-shadow: 0 -1px 1px rgba(0,0,0,0.35);
  }
  .back-button {
    position: absolute; left: 20px; top: 21px; width: 116px; height: 70px;
    border-radius: 6px; border: 1px solid var(--nav-line);
    background: linear-gradient(var(--btn-top), var(--btn-bottom));
    box-shadow: inset 0 1px 0 rgba(255,255,255,0.3), 0 1px 0 rgba(255,255,255,0.2);
    font-family: "Source Sans 3", sans-serif; font-weight: 400; font-size: 36px;
    color: var(--white); text-align: center; line-height: 66px;
    text-shadow: 0 -1px 1px rgba(0,0,0,0.35);
  }

  .video-backdrop {
    position: absolute; left: 0; top: 116px; width: 835px; height: 958px;
    background: linear-gradient(180deg, var(--sky-top) 0%, #a9c4e6 18%, var(--sky-mid) 38%, #e6ecf0 52%, var(--field) 66%, #7f9c5c 82%, var(--grass) 100%);
  }

  .toolbar {
    position: absolute; left: 13px; top: 672px; width: 809px; height: 339px;
    background: var(--panel); border-radius: 9px;
    box-shadow: inset 0 0 0 1px var(--panel-edge);
  }
  .toolbar svg { display: block; width: 809px; height: 339px; }
  .glyph { fill: var(--icon); }
  .cut { fill: var(--icon-cut); }
  .cut-line { stroke: var(--icon-cut); fill: none; }

  .tab-bar {
    position: absolute; left: 0; top: 1074px; width: 835px; height: 126px;
    display: flex; border-top: 1px solid #9a9a9a;
  }
  .tab {
    flex: 1; display: flex; flex-direction: column; align-items: center; justify-content: flex-end;
    padding-bottom: 12px;
    background: linear-gradient(var(--tab-top), var(--tab-bottom));
    border-left: 1px solid var(--tab-divider);
    font-family: "Inter", sans-serif; font-size: 29px; font-weight: 400; color: var(--tab-text);
  }
  .tab:first-child { border-left: none; }
  .tab svg { width: 60px; height: 60px; margin-bottom: 8px; }
  .tab .tab-icon { fill: var(--tab-text); }
  .tab.is-active { background: var(--tab-active); color: var(--white); font-weight: 500; }
  .tab.is-active .tab-icon { fill: var(--white); }
</style>
</head>
<body>
<div class="screen">
  <header class="nav-bar">
    <div class="back-button">Back</div>
    <h1 class="nav-title">Video</h1>
  </header>

  <div class="video-backdrop" role="img" aria-label="Blurred golf video frame: a ball on a tee with a club head under a blue, cloudy sky over green fairway"></div>

  <div class="toolbar">
    <svg viewBox="10 515 620 260" xmlns="http://www.w3.org/2000/svg">
      <!-- Video -->
      <g class="icon-video">
        <rect class="glyph" x="50" y="561" width="29" height="24" rx="3"/>
        <polygon class="glyph" points="79,573 91,563 91,583"/>
      </g>
      <!-- Camera shutter -->
      <g class="icon-camera">
        <rect class="glyph" x="157" y="555" width="14" height="7" rx="2"/>
        <rect class="glyph" x="148" y="559" width="40" height="27" rx="4"/>
        <circle class="cut" cx="168" cy="573" r="10"/>
        <circle class="glyph" cx="168" cy="573" r="6.5"/>
      </g>
      <!-- User -->
      <g class="icon-user">
        <ellipse class="glyph" cx="263" cy="564" rx="8.5" ry="10"/>
        <path class="glyph" d="M245 591 Q245 577 263 577 Q281 577 281 591 Z"/>
      </g>
      <!-- Users -->
      <g class="icon-users">
        <circle class="glyph" cx="351" cy="563" r="7"/>
        <path class="glyph" d="M337 586 Q337 573 351 573 Q360 573 362 578 L358 586 Z"/>
        <circle class="glyph" cx="377" cy="563" r="7"/>
        <path class="glyph" d="M391 586 Q391 573 377 573 Q368 573 366 578 L370 586 Z"/>
        <circle class="cut" cx="364" cy="566" r="9.5"/>
        <circle class="glyph" cx="364" cy="566" r="8"/>
        <path class="cut" d="M347 591 Q347 576 364 576 Q381 576 381 591 Z"/>
        <path class="glyph" d="M349 591 Q349 578 364 578 Q379 578 379 591 Z"/>
      </g>
      <!-- Golfer -->
      <g class="icon-golfer">
        <circle class="glyph" cx="455" cy="562" r="9"/>
        <circle class="cut" cx="455" cy="562" r="5"/>
        <circle class="glyph" cx="455" cy="562" r="2"/>
        <path class="glyph" d="M448 574 L456 574 L462 583 L450 583 Z"/>
        <path class="glyph" d="M485 553 L488 555 L466 586 Q460 592 451 590 L449 587 Q458 586 462 582 Z"/>
      </g>
      <!-- Help (lifebuoy) -->
      <g class="icon-help">
        <circle class="glyph" cx="566" cy="572" r="20"/>
        <circle class="cut" cx="566" cy="572" r="11"/>
        <circle class="glyph" cx="566" cy="572" r="9"/>
        <circle class="cut-line" cx="566" cy="572" r="15.5" stroke-width="2" stroke-dasharray="12 12.3" stroke-dashoffset="6"/>
        <circle class="cut" cx="566" cy="572" r="7"/>
      </g>
      <!-- Favorite -->
      <polygon class="glyph icon-favorite" points="70,625 75.5,638 89,639 78.5,648 82,662 70,654.5 58,662 61.5,648 51,639 64.5,638"/>
      <!-- Next -->
      <g class="icon-next">
        <circle class="glyph" cx="168" cy="644" r="18"/>
        <path class="cut" d="M157 640 L168 640 L168 633 L180 644 L168 655 L168 648 L157 648 Z"/>
      </g>
      <!-- Previous -->
      <g class="icon-previous">
        <circle class="glyph" cx="263" cy="645" r="18"/>
        <path class="cut" d="M274 641 L263 641 L263 634 L251 645 L263 656 L263 649 L274 649 Z"/>
      </g>
      <!-- Log-in (lock) -->
      <g class="icon-login">
        <path d="M355 643 L355 635 Q355 625 364 625 Q373 625 373 635 L373 643" fill="none" stroke="#d2d2d2" stroke-width="4"/>
        <rect class="glyph" x="348" y="641" width="32" height="22" rx="3"/>
        <circle class="cut" cx="364" cy="650" r="3"/>
        <rect class="cut" x="362.5" y="650" width="3" height="7"/>
      </g>
      <!-- Sign-up (user add) -->
      <g class="icon-signup">
        <ellipse class="glyph" cx="462" cy="636" rx="8.5" ry="10"/>
        <path class="glyph" d="M444 663 Q444 648 462 648 Q480 648 480 663 Z"/>
        <circle class="cut" cx="477" cy="657" r="9"/>
        <circle class="glyph" cx="477" cy="657" r="7.5"/>
        <rect class="cut" x="472" y="656" width="10" height="2.4"/>
        <rect class="cut" x="475.8" y="652" width="2.4" height="10"/>
      </g>
      <!-- Password (key) -->
      <g class="icon-password">
        <circle class="glyph" cx="577" cy="635" r="10"/>
        <circle class="cut" cx="580" cy="632" r="3"/>
        <path class="glyph" d="M568 638 L574 644 L553 665 L547 659 Z"/>
        <path class="glyph" d="M553 657 L558 662 L555 665 L550 660 Z M558 652 L563 657 L560 660 L555 655 Z"/>
      </g>
      <!-- Question -->
      <g class="icon-question">
        <circle class="glyph" cx="70" cy="720" r="18"/>
        <text x="70" y="730" text-anchor="middle" font-family="Source Sans 3, sans-serif" font-weight="700" font-size="28" class="cut">?</text>
      </g>
    </svg>
  </div>

  <nav class="tab-bar">
    <div class="tab is-active">
      <svg viewBox="0 0 40 40" aria-hidden="true">
        <rect class="tab-icon" x="6" y="2" width="3" height="36"/>
        <path class="tab-icon" d="M10 4 Q20 1 26 5 Q31 8 36 6 L36 22 Q31 24 26 21 Q20 17 10 20 Z"/>
      </svg>
      <span>Main</span>
    </div>
    <div class="tab">
      <svg viewBox="0 0 40 40" aria-hidden="true">
        <rect class="tab-icon" x="19" y="1" width="1.6" height="13"/>
        <polygon class="tab-icon" points="20.6,1 28,4 20.6,7"/>
        <path class="tab-icon" d="M20 13 L36 27 L33 29 L20 18 L7 29 L4 27 Z"/>
        <path class="tab-icon" d="M9 27 L20 18 L31 27 L31 38 L9 38 Z M17 30 L17 38 L23 38 L23 30 Z"/>
      </svg>
      <span>Clubhouse</span>
    </div>
    <div class="tab">
      <svg viewBox="0 0 40 40" aria-hidden="true">
        <path class="tab-icon" fill-rule="evenodd" d="M17 2 L23 2 L24 8 L28 10 L33 6 L37 11 L33 15 L35 19 L40 20 L38 26 L33 26 L31 30 L35 35 L30 39 L26 34 L22 36 L21 40 L15 40 L15 35 L11 33 L6 37 L2 32 L6 28 L4 24 L0 23 L1 17 L6 17 L8 13 L4 8 L9 4 L13 8 L17 6 Z M20 13 A8 8 0 1 0 20.01 13 Z"/>
      </svg>
      <span>Setting</span>
    </div>
  </nav>
</div>
</body>
</html>
```